Brixel Solutions Website Creation

Create a business website for custom flexible packaging and MDF products. The www.Olvane.com website is generic page that you can use to create a similar home page for my business.
Specifically: https://www.olvane.com/packaging/
https://www.olvane.com/product/mdf-panels/
Domain is Brix-El.com
I would like the page to have a more packaging related look than the MDF/wood.

```html
<!DOCTYPE html>
<html lang="en">
<head>
<meta charset="utf-8">
<title>Brixel Solutions — Custom Flexible Packaging</title>
<link href="https://fonts.googleapis.com/css2?family=Plus+Jakarta+Sans:wght@500;600;700;800&family=Inter:wght@400;500;600&display=swap" rel="stylesheet">
<style>
:root{
  --navy:#1d2a52;
  --navy-deep:#17224a;
  --blue:#0ea5f0;
  --blue-strong:#1d7fe0;
  --sky:#dff3fc;
  --mist:#f1f5f9;
  --ink:#1a2238;
  --text:#5b6476;
  --muted:#8a93a6;
  --line:#e6eaf0;
  --white:#ffffff;
}
*{box-sizing:border-box;margin:0;padding:0}
html,body{width:1200px;height:4552px;overflow:hidden}
body{font-family:"Inter",sans-serif;color:var(--text);background:var(--white);font-size:11px;line-height:1.6}
h1,h2,h3,h4,.display{font-family:"Plus Jakarta Sans",sans-serif;color:var(--ink);font-weight:800;letter-spacing:-.02em}
.wrap{width:760px;margin:0 auto;position:relative}
.eyebrow{font-size:8px;letter-spacing:.2em;font-weight:600;color:var(--blue);text-transform:uppercase}
.btn{display:inline-flex;align-items:center;gap:6px;height:28px;padding:0 18px;border-radius:20px;font-size:9px;font-weight:600;font-family:"Inter",sans-serif}
.btn-blue{background:var(--blue-strong);color:#fff}
.btn-navy{background:var(--navy);color:#fff}
.btn-ghost{border:1px solid rgba(255,255,255,.35);color:#fff;background:rgba(255,255,255,.08)}
.btn-white{background:#fff;color:var(--navy)}
.brand{display:flex;align-items:center;gap:7px;font-family:"Plus Jakarta Sans",sans-serif;font-weight:700;font-size:14px;color:var(--blue-strong)}
.brand-dot{width:22px;height:22px;border-radius:50%;background:var(--blue-strong)}

/* nav */
.site-nav{height:53px;border-bottom:1px solid var(--line);background:#fff}
.site-nav .wrap{display:flex;align-items:center;height:53px}
.site-nav ul{margin-left:auto;display:flex;gap:22px;list-style:none;font-size:9px;color:var(--ink);align-items:center}
.site-nav .btn{height:24px;padding:0 13px;margin-left:22px}

/* hero */
.hero{height:518px;position:relative;background:linear-gradient(180deg,#2b3e74 0%,#27407c 45%,#1f3163 100%);text-align:center;color:#fff;overflow:hidden}
.hero-photo{position:absolute;inset:0;background:radial-gradient(ellipse at 20% 30%,rgba(90,130,200,.35),transparent 55%),radial-gradient(ellipse at 80% 70%,rgba(70,110,190,.3),transparent 55%)}
.hero-inner{position:relative;padding-top:124px}
.pill{display:inline-block;border:1px solid rgba(255,255,255,.4);border-radius:20px;padding:4px 14px;font-size:9px;letter-spacing:.22em;font-weight:600;background:rgba(255,255,255,.08)}
.hero h1{color:#fff;font-size:46px;line-height:48px;margin-top:16px}
.hero h1 .accent{background:linear-gradient(90deg,#7cc8ff,#3fa9f5);-webkit-background-clip:text;background-clip:text;color:transparent}
.hero p{width:420px;margin:18px auto 0;font-size:10.5px;line-height:17px;color:rgba(255,255,255,.88)}
.hero-actions{display:flex;gap:10px;justify-content:center;margin-top:28px}
.stats{display:flex;justify-content:center;gap:58px;margin-top:54px}
.stat strong{display:block;font-family:"Plus Jakarta Sans",sans-serif;font-size:19px;font-weight:800;line-height:22px}
.stat span{font-size:7px;letter-spacing:.12em;color:rgba(255,255,255,.7);text-transform:uppercase}

/* about */
.about{height:481px}
.about .wrap{display:flex;justify-content:space-between;padding-top:91px}
.about-copy{width:350px}
.about h2{font-size:30px;line-height:31px;margin-top:10px}
.rule{width:40px;height:2px;background:var(--blue);margin:20px 0 24px}
.about p{font-size:9.5px;line-height:16px;margin-bottom:10px}
.checks{display:grid;grid-template-columns:1fr 1fr;gap:10px 0;margin-top:14px;font-size:8.5px;color:var(--ink)}
.checks li{list-style:none;display:flex;align-items:center;gap:7px}
.tick{width:12px;height:12px;border-radius:50%;background:#e1f2fd;display:inline-flex;align-items:center;justify-content:center}
.about-media{position:relative;width:355px;margin-top:24px}
.photo{background:linear-gradient(160deg,#b7a58c,#8b7c6a 40%,#c9bba6);border-radius:10px}
.about-media .photo{height:265px;box-shadow:0 12px 30px rgba(14,165,240,.25)}
.badge{position:absolute;left:-15px;top:228px;width:156px;height:51px;background:#fff;border-radius:8px;box-shadow:0 8px 20px rgba(20,30,60,.12);display:flex;align-items:center;gap:10px;padding:0 12px}
.badge-icon{width:24px;height:24px;border-radius:50%;background:var(--blue-strong);display:flex;align-items:center;justify-content:center}
.badge strong{display:block;font-family:"Plus Jakarta Sans",sans-serif;font-size:11px;color:var(--ink);line-height:13px}
.badge span{font-size:7px;color:var(--muted)}

/* why */
.why{height:433px;background:var(--mist);text-align:center}
.why .wrap{padding-top:75px}
.why h2{font-size:23px;line-height:25px;margin-top:10px}
.why .lead{width:380px;margin:14px auto 0;font-size:9.5px;line-height:15px}
.features{display:grid;grid-template-columns:repeat(4,1fr);gap:17px;margin-top:38px;text-align:left}
.feature{background:#fff;border-radius:10px;height:142px;padding:18px 17px;box-shadow:0 2px 8px rgba(20,30,60,.05)}
.feature-icon{width:26px;height:26px;border-radius:7px;background:#e3f3fd;display:flex;align-items:center;justify-content:center}
.feature h3{font-size:11px;font-weight:700;margin:16px 0 6px;letter-spacing:0}
.feature p{font-size:8px;line-height:13px}
.feature.is-active{background:var(--blue);color:#fff}
.feature.is-active h3{color:#fff}
.feature.is-active .feature-icon{background:var(--navy)}

/* products */
.products{height:706px}
.products .wrap{padding-top:50px}
.products h2{font-size:29px;line-height:32px;margin-top:8px}
.products-head{display:flex;justify-content:space-between;align-items:flex-end;margin-top:8px;font-size:9.5px}
.products-head a{color:var(--blue-strong);font-size:8px;font-weight:600;text-decoration:none}
.grid{display:grid;grid-template-columns:repeat(3,240px);gap:19px 20px;margin-top:38px}
.tile{height:219px;border-radius:6px;position:relative;overflow:hidden}
.tile .photo{position:absolute;inset:0;border-radius:0}
.tile::after{content:"";position:absolute;inset:0;background:linear-gradient(180deg,transparent 55%,rgba(20,30,60,.7))}
.tile h3{position:absolute;left:0;right:0;bottom:14px;text-align:center;color:#fff;font-size:14px;font-weight:700;z-index:1;letter-spacing:0}
.tile-arrow{position:absolute;top:-6px;right:-6px;width:56px;height:56px;border-radius:50%;background:#fff;z-index:1;display:flex;align-items:center;justify-content:center}
.tile-arrow span{width:38px;height:38px;border-radius:50%;background:var(--blue-strong);display:flex;align-items:center;justify-content:center}
.tile-cta{background:var(--navy);text-align:center;padding:32px 22px 0;color:#c9d2e6}
.tile-cta::after{display:none}
.tile-cta h3{position:static;font-size:19px;line-height:24px}
.tile-cta p{font-size:8.5px;line-height:14px;margin:10px 0 24px}
.tile-cta .btn{height:32px;padding:0 44px}

/* sustainability */
.sustain{height:472px;background:var(--sky)}
.sustain .wrap{display:flex;justify-content:space-between;padding-top:88px}
.sustain-media{width:355px;height:265px;margin-top:16px;background:linear-gradient(150deg,#f3f1ec,#d7b98c 50%,#e8e4da);border-radius:10px;box-shadow:0 10px 26px rgba(20,30,60,.12)}
.sustain-copy{width:355px}
.tag{display:inline-flex;align-items:center;gap:4px;background:#fff;border-radius:10px;padding:2px 8px;font-size:7px;letter-spacing:.18em;color:var(--blue);font-weight:600}
.sustain h2{font-size:29px;line-height:30px;margin-top:8px}
.sustain p{font-size:9.5px;line-height:16px;margin-top:14px}
.chips{display:grid;grid-template-columns:1fr 1fr;gap:10px;margin-top:22px}
.chip{background:#fff;height:28px;border-radius:6px;display:flex;align-items:center;gap:8px;padding:0 10px;font-size:8px;font-weight:600;color:var(--ink)}
.chip .dot{width:14px;height:14px;border-radius:50%;background:var(--blue-strong);display:flex;align-items:center;justify-content:center}
.sustain .btn{margin-top:22px;height:28px}

/* mdf */
.mdf{height:380px}
.mdf .wrap{padding-top:62px}
.mdf-card{display:flex;height:258px;border-radius:10px;overflow:hidden;box-shadow:0 6px 24px rgba(20,30,60,.08);border:1px solid var(--line)}
.mdf-media{width:400px;background:linear-gradient(170deg,#3d3a3a,#8c7256 45%,#d6c0a0 70%,#b49772)}
.mdf-copy{padding:40px 34px}
.mdf h2{font-size:22px;margin:10px 0 16px}
.mdf p{font-size:9.5px;line-height:16px;width:290px}
.mdf .btn{margin-top:20px}

/* testimonials */
.testimonials{height:403px;background:var(--navy);text-align:center}
.testimonials .wrap{padding-top:76px}
.testimonials h2{color:#fff;font-size:22px;line-height:25px;margin-top:6px}
.quotes{display:flex;justify-content:center;gap:14px;margin-top:44px;text-align:left}
.quote{width:333px;height:150px;border-radius:10px;background:rgba(255,255,255,.06);border:1px solid rgba(255,255,255,.1);padding:18px 20px}
.stars{color:var(--blue);font-size:11px;letter-spacing:2px}
.quote p{color:#e6ebf5;font-size:12px;line-height:20px;margin:10px 0 10px}
.quote span{font-size:7.5px;color:#8d9bbb}

/* cta */
.cta{height:314px;position:relative;text-align:center;background:linear-gradient(120deg,#1f3b7a,#2360b0 60%,#2a79d6);overflow:hidden}
.cta-photo{position:absolute;inset:0;background:radial-gradient(ellipse at 25% 60%,rgba(120,170,240,.25),transparent 55%)}
.cta-inner{position:relative;padding-top:90px;color:#fff}
.cta h2{color:#fff;font-size:29px;line-height:29px;width:560px;margin:0 auto}
.cta p{font-size:9.5px;line-height:15px;width:420px;margin:14px auto 0;color:rgba(255,255,255,.85)}
.cta-actions{display:flex;gap:8px;justify-content:center;margin-top:18px}

/* contact */
.contact{height:537px}
.contact .wrap{display:flex;justify-content:space-between;padding-top:82px}
.contact-copy{width:357px}
.contact h2{font-size:29px;line-height:30px;margin-top:10px}
.contact-copy>p{font-size:9.5px;line-height:15px;margin-top:14px}
.contact-card{margin-top:28px;border:1px solid var(--line);border-radius:10px;box-shadow:0 6px 20px rgba(20,30,60,.07);padding:20px}
.person{display:flex;align-items:center;gap:12px}
.avatar{width:34px;height:34px;border-radius:8px;background:var(--blue-strong);color:#fff;font-weight:700;font-size:11px;display:flex;align-items:center;justify-content:center;font-family:"Plus Jakarta Sans",sans-serif}
.person strong{display:block;font-size:11px;color:var(--ink);font-family:"Plus Jakarta Sans",sans-serif}
.person span{font-size:7.5px;color:var(--muted)}
.field{margin-top:10px;background:var(--mist);border-radius:8px;height:40px;display:flex;align-items:center;gap:14px;padding:0 14px}
.field small{display:block;font-size:6.5px;letter-spacing:.12em;color:var(--muted);font-weight:600;line-height:9px}
.field b{font-size:10px;color:var(--ink);font-weight:600}
.contact-card .btn{width:100%;justify-content:center;margin-top:18px;height:30px;background:linear-gradient(90deg,#0ea5f0,#1d6fd8);color:#fff}
.map{width:355px;height:378px;border-radius:10px;background:radial-gradient(ellipse at 50% 75%,#bcd0f3,transparent 55%),linear-gradient(160deg,#dbe9fb,#eef3fb 50%,#e2ebf9);box-shadow:0 6px 20px rgba(20,30,60,.07);text-align:center;padding-top:146px}
.map-pin{width:36px;height:36px;border-radius:10px;background:#fff;margin:0 auto;display:flex;align-items:center;justify-content:center}
.map h3{font-size:14px;font-weight:700;margin-top:18px;letter-spacing:0}
.map p{font-size:8px;line-height:12px;width:240px;margin:8px auto 0}

/* footer */
.site-footer{height:255px;background:var(--navy);color:#aeb8d0}
.site-footer .wrap{padding-top:45px}
.footer-cols{display:grid;grid-template-columns:196px 196px 197px 171px}
.site-footer .brand{color:#7cc6f7}
.footer-cols p{font-size:8px;line-height:12px;margin-top:10px;width:160px}
.site-footer h4{color:#aeb8d0;font-size:7.5px;letter-spacing:.16em;font-family:"Inter",sans-serif;font-weight:600;margin:6px 0 12px}
.site-footer ul{list-style:none;font-size:8px;line-height:19px;color:#d6dcea}
.site-footer ul li{display:flex;align-items:center;gap:6px}
.footer-bottom{margin-top:52px;border-top:1px solid rgba(255,255,255,.1);padding-top:12px;display:flex;justify-content:space-between;font-size:7px;color:#7f8bab}
</style>
</head>
<body>

<header class="site-nav">
  <div class="wrap">
    <div class="brand"><span class="brand-dot"></span>Brixel Solutions</div>
    <ul>
      <li>Home</li><li>Packaging</li><li>MDF Products</li><li>About</li><li>Contact</li>
    </ul>
    <a class="btn btn-blue">Request a Quote</a>
  </div>
</header>

<section class="hero">
  <div class="hero-photo" role="img" aria-label="Industrial packaging factory floor with production lines"></div>
  <div class="hero-inner">
    <span class="pill">GLOBAL PACKAGING PARTNER</span>
    <h1>Custom Flexible<br><span class="accent">Packaging Solutions</span></h1>
    <p>Delivering innovative, high-quality flexible packaging products for food, agriculture, industrial, healthcare, and consumer markets. Your trusted global sourcing partner for packaging and MDF solutions.</p>
    <div class="hero-actions">
      <a class="btn btn-blue">Request a Quote
        <svg width="9" height="9" viewBox="0 0 10 10"><path d="M1 5h8M6 2l3 3-3 3" stroke="#fff" stroke-width="1.4" fill="none"/></svg></a>
      <a class="btn btn-ghost">Explore Products</a>
    </div>
    <div class="stats">
      <div class="stat"><strong>25+</strong><span>Years Experience</span></div>
      <div class="stat"><strong>500+</strong><span>Industry Partners</span></div>
      <div class="stat"><strong>50+</strong><span>Product Lines</span></div>
      <div class="stat"><strong>100%</strong><span>Quality Focused</span></div>
    </div>
  </div>
</section>

<section class="about">
  <div class="wrap">
    <div class="about-copy">
      <div class="eyebrow">About Brixel</div>
      <h2>A Global Packaging Partner You Can Trust</h2>
      <div class="rule"></div>
      <p>Brixel Solutions delivers innovative flexible packaging products and industrial packaging solutions to businesses across multiple industries. Our commitment to quality, reliability, and customer-focused service enables us to provide packaging products that protect, preserve, and promote your products while optimizing your supply chain.</p>
      <p>Whether you require custom flexible packaging, stretch films, industrial supplies, or MDF products, Brixel is dedicated to delivering solutions tailored to your business needs.</p>
      <ul class="checks">
        <li><span class="tick"><svg width="7" height="7" viewBox="0 0 10 10"><path d="M2 5l2 2 4-4" stroke="#0ea5f0" stroke-width="1.6" fill="none"/></svg></span>Custom-engineered solutions</li>
        <li><span class="tick"><svg width="7" height="7" viewBox="0 0 10 10"><path d="M2 5l2 2 4-4" stroke="#0ea5f0" stroke-width="1.6" fill="none"/></svg></span>Rigorous quality control</li>
        <li><span class="tick"><svg width="7" height="7" viewBox="0 0 10 10"><path d="M2 5l2 2 4-4" stroke="#0ea5f0" stroke-width="1.6" fill="none"/></svg></span>Reliable supply chain</li>
        <li><span class="tick"><svg width="7" height="7" viewBox="0 0 10 10"><path d="M2 5l2 2 4-4" stroke="#0ea5f0" stroke-width="1.6" fill="none"/></svg></span>Dedicated account support</li>
      </ul>
    </div>
    <div class="about-media">
      <div class="photo" role="img" aria-label="Warehouse aisle with tall racks of packaged cartons"></div>
      <div class="badge">
        <span class="badge-icon"><svg width="11" height="11" viewBox="0 0 12 12"><rect x="2" y="2" width="8" height="8" rx="1.5" stroke="#fff" stroke-width="1.3" fill="none"/><path d="M4 5h4" stroke="#fff" stroke-width="1.3"/></svg></span>
        <div><strong>50+ Lines</strong><span>Packaging &amp; MDF products</span></div>
      </div>
    </div>
  </div>
</section>

<section class="why">
  <div class="wrap">
    <div class="eyebrow">Why choose Brixel</div>
    <h2>Built on quality, delivered<br>with reliability</h2>
    <p class="lead">Everything we do is engineered to protect your products, streamline your operations, and grow with your business.</p>
    <div class="features">
      <div class="feature">
        <div class="feature-icon"><svg width="12" height="12" viewBox="0 0 12 12"><circle cx="6" cy="6" r="4.5" stroke="#0ea5f0" stroke-width="1.2" fill="none"/><path d="M1.5 6h9M6 1.5c2 2 2 7 0 9M6 1.5c-2 2-2 7 0 9" stroke="#0ea5f0" stroke-width="1" fill="none"/></svg></div>
        <h3>Global Sourcing</h3>
        <p>Reliable sourcing network delivering quality packaging solutions worldwide.</p>
      </div>
      <div class="feature is-active">
        <div class="feature-icon"><svg width="12" height="12" viewBox="0 0 12 12"><path d="M6 1l4 1.5V6c0 2.5-2 4-4 5-2-1-4-2.5-4-5V2.5z" stroke="#fff" stroke-width="1.2" fill="none"/></svg></div>
        <h3>Premium Quality</h3>
        <p>Consistent products manufactured to meet demanding industry standards.</p>
      </div>
      <div class="feature">
        <div class="feature-icon"><svg width="12" height="12" viewBox="0 0 12 12"><path d="M1 3h6v5H1zM7 5h2.5L11 7v1H7z" stroke="#0ea5f0" stroke-width="1.1" fill="none"/><circle cx="3" cy="9" r="1" fill="#0ea5f0"/><circle cx="9" cy="9" r="1" fill="#0ea5f0"/></svg></div>
        <h3>Fast Delivery</h3>
        <p>Efficient logistics and dependable supply chain management.</p>
      </div>
      <div class="feature">
        <div class="feature-icon"><svg width="12" height="12" viewBox="0 0 12 12"><path d="M2 10C2 5 5 2 10 2c0 5-3 8-8 8zM2 10l5-5" stroke="#0ea5f0" stroke-width="1.2" fill="none"/></svg></div>
        <h3>Sustainable Solutions</h3>
        <p>Eco-friendly packaging materials and recyclable product options.</p>
      </div>
    </div>
  </div>
</section>

<section class="products">
  <div class="wrap">
    <div class="eyebrow">Product portfolio</div>
    <h2>Our Packaging Solutions</h2>
    <div class="products-head">
      <span>Comprehensive packaging products designed to protect, preserve, and perform.</span>
      <a>Ask about custom orders →</a>
    </div>
    <div class="grid">
      <div class="tile">
        <div class="photo" style="background:linear-gradient(160deg,#d9dde3,#a9b0ba 50%,#6d7480)" role="img" aria-label="Silver stand-up pouch with dried goods"></div>
        <div class="tile-arrow"><span><svg width="12" height="12" viewBox="0 0 12 12"><path d="M3 9l6-6M4 3h5v5" stroke="#fff" stroke-width="1.4" fill="none"/></svg></span></div>
        <h3>Flexible Packaging</h3>
      </div>
      <div class="tile">
        <div class="photo" style="background:linear-gradient(160deg,#8d6b55,#c7c3c0 45%,#e1e1e3 70%,#8f949c)" role="img" aria-label="Rolls of stretch film in a warehouse"></div>
        <div class="tile-arrow"><span><svg width="12" height="12" viewBox="0 0 12 12"><path d="M3 9l6-6M4 3h5v5" stroke="#fff" stroke-width="1.4" fill="none"/></svg></span></div>
        <h3>Stretch Film</h3>
      </div>
      <div class="tile">
        <div class="photo" style="background:linear-gradient(150deg,#eceef1,#e0b43c 40%,#2a2c30 60%,#a13a2e)" role="img" aria-label="Work gloves and protective safety supplies"></div>
        <div class="tile-arrow"><span><svg width="12" height="12" viewBox="0 0 12 12"><path d="M3 9l6-6M4 3h5v5" stroke="#fff" stroke-width="1.4" fill="none"/></svg></span></div>
        <h3>Safety Supplies</h3>
      </div>
      <div class="tile">
        <div class="photo" style="background:linear-gradient(165deg,#a88a68,#cfcfcc 45%,#8d939a 75%,#5a5f66)" role="img" aria-label="Coils of strapping and banding material"></div>
        <div class="tile-arrow"><span><svg width="12" height="12" viewBox="0 0 12 12"><path d="M3 9l6-6M4 3h5v5" stroke="#fff" stroke-width="1.4" fill="none"/></svg></span></div>
        <h3>Strapping &amp; Banding</h3>
      </div>
      <div class="tile">
        <div class="photo" style="background:linear-gradient(170deg,#e7ecef,#4fb3d3 40%,#2a8fb2 70%,#c7cdd2)" role="img" aria-label="Stacked teal shipping boxes"></div>
        <div class="tile-arrow"><span><svg width="12" height="12" viewBox="0 0 12 12"><path d="M3 9l6-6M4 3h5v5" stroke="#fff" stroke-width="1.4" fill="none"/></svg></span></div>
        <h3>Other Packaging</h3>
      </div>
      <div class="tile tile-cta">
        <h3>Need a Custom Packaging Solution?</h3>
        <p>We offer a wide range of custom and specialty packaging products beyond our standard portfolio.</p>
        <a class="btn btn-blue">Request a Quote</a>
      </div>
    </div>
  </div>
</section>

<section class="sustain">
  <div class="wrap">
    <div class="sustain-media" role="img" aria-label="Kraft paper pouches with green leaves"></div>
    <div class="sustain-copy">
      <span class="tag"><svg width="7" height="7" viewBox="0 0 12 12"><path d="M2 10C2 5 5 2 10 2c0 5-3 8-8 8z" stroke="#0ea5f0" stroke-width="1.5" fill="none"/></svg>SUSTAINABILITY</span>
      <h2>Sustainable Packaging for a Better Tomorrow</h2>
      <p>Brixel is committed to providing environmentally responsible packaging solutions. We offer recyclable materials, eco-friendly packaging options, and innovative products designed to reduce waste while maintaining exceptional performance.</p>
      <div class="chips">
        <div class="chip"><span class="dot"><svg width="7" height="7" viewBox="0 0 10 10"><path d="M2 5l2 2 4-4" stroke="#fff" stroke-width="1.6" fill="none"/></svg></span>Recyclable Materials</div>
        <div class="chip"><span class="dot"><svg width="7" height="7" viewBox="0 0 10 10"><path d="M2 5l2 2 4-4" stroke="#fff" stroke-width="1.6" fill="none"/></svg></span>Green Packaging Options</div>
        <div class="chip"><span class="dot"><svg width="7" height="7" viewBox="0 0 10 10"><path d="M2 5l2 2 4-4" stroke="#fff" stroke-width="1.6" fill="none"/></svg></span>Reduced Plastic Waste</div>
        <div class="chip"><span class="dot"><svg width="7" height="7" viewBox="0 0 10 10"><path d="M2 5l2 2 4-4" stroke="#fff" stroke-width="1.6" fill="none"/></svg></span>Sustainable Supply Chain</div>
      </div>
      <a class="btn btn-navy">Explore Sustainable Solutions
        <svg width="9" height="9" viewBox="0 0 10 10"><path d="M1 5h8M6 2l3 3-3 3" stroke="#fff" stroke-width="1.4" fill="none"/></svg></a>
    </div>
  </div>
</section>

<section class="mdf">
  <div class="wrap">
    <div class="mdf-card">
      <div class="mdf-media" role="img" aria-label="Stacks of MDF panels in a factory hall"></div>
      <div class="mdf-copy">
        <div class="eyebrow">Supporting category</div>
        <h2>MDF Products</h2>
        <p>In addition to packaging solutions, Brixel also supplies premium MDF panels and engineered wood products for industrial, commercial, and manufacturing applications.</p>
        <a class="btn btn-navy">View MDF Products
          <svg width="9" height="9" viewBox="0 0 10 10"><path d="M1 5h8M6 2l3 3-3 3" stroke="#fff" stroke-width="1.4" fill="none"/></svg></a>
      </div>
    </div>
  </div>
</section>

<section class="testimonials">
  <div class="wrap">
    <div class="eyebrow">Testimonials</div>
    <h2>Trusted by Businesses Across<br>Industries</h2>
    <div class="quotes">
      <div class="quote">
        <div class="stars">★★★★★</div>
        <p>"Brixel consistently delivers outstanding packaging products with dependable service and exceptional quality."</p>
        <span>— Manufacturing Customer</span>
      </div>
      <div class="quote">
        <div class="stars">★★★★★</div>
        <p>"Their custom packaging solutions have helped improve our product presentation while reducing shipping costs."</p>
        <span>— Food Industry Client</span>
      </div>
    </div>
  </div>
</section>

<section class="cta">
  <div class="cta-photo" role="img" aria-label="Workers in a packaging production facility"></div>
  <div class="cta-inner">
    <h2>Ready to Upgrade Your Packaging Solutions?</h2>
    <p>Partner with Brixel to discover innovative packaging products designed to meet your business goals.</p>
    <div class="cta-actions">
      <a class="btn btn-white">Request a Quote
        <svg width="9" height="9" viewBox="0 0 10 10"><path d="M1 5h8M6 2l3 3-3 3" stroke="#1d2a52" stroke-width="1.4" fill="none"/></svg></a>
      <a class="btn btn-ghost">Contact Our Team</a>
    </div>
  </div>
</section>

<section class="contact">
  <div class="wrap">
    <div class="contact-copy">
      <div class="eyebrow">Get in touch</div>
      <h2>Let's build your packaging program</h2>
      <p>Reach out to speak with our team about custom quotes, product samples, or supply-chain support.</p>
      <div class="contact-card">
        <div class="person">
          <span class="avatar">DW</span>
          <div><strong>Dalen Whitcombe</strong><span>Owner</span></div>
        </div>
        <div class="field">
          <svg width="11" height="11" viewBox="0 0 12 12"><path d="M3 1.5l2 2.5-1 1.2c.6 1.3 1.5 2.2 2.8 2.8L8 7l2.5 2-1 1.5C5.5 10.5 1.5 6.5 1.5 2.5z" stroke="#1d7fe0" stroke-width="1" fill="none"/></svg>
          <div><small>MOBILE</small><b>555-014-2287</b></div>
        </div>
        <div class="field">
          <svg width="11" height="11" viewBox="0 0 12 12"><rect x="1.5" y="2.5" width="9" height="7" rx="1" stroke="#1d7fe0" stroke-width="1" fill="none"/><path d="M1.5 3l4.5 3.5L10.5 3" stroke="#1d7fe0" stroke-width="1" fill="none"/></svg>
          <div><small>EMAIL</small><b>Dalen.Whitcombe@Brix-El.com</b></div>
        </div>
        <a class="btn">Request a Quote
          <svg width="9" height="9" viewBox="0 0 10 10"><path d="M1 5h8M6 2l3 3-3 3" stroke="#fff" stroke-width="1.4" fill="none"/></svg></a>
      </div>
    </div>
    <div class="map">
      <div class="map-pin"><svg width="14" height="14" viewBox="0 0 12 12"><path d="M6 11s4-3.6 4-6.5a4 4 0 0 0-8 0C2 7.4 6 11 6 11z" stroke="#1d7fe0" stroke-width="1.1" fill="none"/><circle cx="6" cy="4.5" r="1.4" stroke="#1d7fe0" stroke-width="1.1" fill="none"/></svg></div>
      <h3>Serving businesses nationwide</h3>
      <p>Brixel partners with clients across the United States and abroad, delivering packaging products where and when you need them.</p>
    </div>
  </div>
</section>

<footer class="site-footer">
  <div class="wrap">
    <div class="footer-cols">
      <div>
        <div class="brand"><span class="brand-dot" style="background:#7cc6f7"></span>Brixel Solutions</div>
        <p>Global sourcing partner for custom flexible packaging, industrial supplies and MDF products.</p>
      </div>
      <div>
        <h4>NAVIGATION</h4>
        <ul><li>Home</li><li>Packaging</li><li>MDF Products</li><li>About</li><li>Contact</li></ul>
      </div>
      <div>
        <h4>PRODUCTS</h4>
        <ul><li>Flexible Packaging</li><li>Stretch Film</li><li>Safety Supplies</li><li>Strapping</li><li>Other Packaging</li></ul>
      </div>
      <div>
        <h4>CONTACT</h4>
        <ul>
          <li style="font-weight:600">Dalen Whitcombe</li>
          <li><svg width="9" height="9" viewBox="0 0 12 12"><path d="M3 1.5l2 2.5-1 1.2c.6 1.3 1.5 2.2 2.8 2.8L8 7l2.5 2-1 1.5C5.5 10.5 1.5 6.5 1.5 2.5z" stroke="#d6dcea" stroke-width="1.1" fill="none"/></svg>555-014-2287</li>
          <li><svg width="9" height="9" viewBox="0 0 12 12"><rect x="1.5" y="2.5" width="9" height="7" rx="1" stroke="#d6dcea" stroke-width="1.1" fill="none"/><path d="M1.5 3l4.5 3.5L10.5 3" stroke="#d6dcea" stroke-width="1.1" fill="none"/></svg>Dalen.Whitcombe@Brix-El.com</li>
        </ul>
      </div>
    </div>
    <div class="footer-bottom">
      <span>© 2025 Brixel Solutions. All Rights Reserved.</span>
      <span>Custom Flexible Packaging · Industrial Supplies · MDF Products</span>
    </div>
  </div>
</footer>

</body>
</html>
```